I need a professional business card to handout at networking events for my senior helper business. I would like to use the logo I have uploaded. The design should be clear and easy to read and should list the following information...
Dessa Quillan
Owner
www.BrightwayElderAssist.example
Cedarvale, Texas
555.304.2291
Dessa@brightwayelderassist.example

Target Market(s)

Senior Citizens

Industry/Entity Type

Personal Helper/ Assisstant

Contact Information for Business Card

I have included the details in the project description box.

Font styles to use
Serif

Colors
0054AA
0677BA
7BADD7
CADEEF
E8F1F8
59FF00
82FF00
B8FF75
E3FFCB
F4FFEA
E54698
E96AAD
F1A4CE
F9D9EA
FCEFF6
6B429C
8869AF
B7A5CE
E3DAEB
F3F0F8

Requirements
Must have
• Include uploaded logo
Nice to have
• The log that has been uploaded
Should not have
• No crazy fonts

```html
<!DOCTYPE html>
<html lang="en">
<head>
<meta charset="utf-8">
<title>Brightway Elder Assist – Business Card</title>
<link rel="stylesheet" href="https://fonts.googleapis.com/css2?family=Didact+Gothic&family=Questrial&display=swap">
<style>
  :root {
    --stage: #e9e8ee;
    --purple: #5f54a8;
    --ink-purple: #5a4aa6;
    --rose: #d0185c;
    --teal: #17989a;
    --white: #ffffff;
    --edge: #c8175a;
  }
  * { box-sizing: border-box; margin: 0; padding: 0; }
  html, body { width: 1200px; height: 801px; overflow: hidden; }
  body {
    background: var(--stage);
    font-family: "Didact Gothic", "Questrial", sans-serif;
    position: relative;
  }
  .card {
    position: absolute;
    top: 235px;
    width: 540px;
    height: 309px;
    border-radius: 16px;
    border-bottom: 3px solid var(--edge);
    box-shadow: 0 6px 18px rgba(40, 30, 70, 0.18);
    overflow: hidden;
  }
  .card--front { left: 40px; background: var(--purple); }
  .card--back { left: 620px; background: var(--white); }

  .wordmark {
    position: absolute;
    display: flex;
    align-items: center;
    gap: 12px;
  }
  .wordmark__dot {
    width: 18px; height: 18px; border-radius: 50%;
    background: var(--rose);
    flex: none;
  }
  .wordmark__name { line-height: 1.05; }
  .wordmark__main { display: block; font-size: 40px; letter-spacing: 0.5px; }
  .wordmark__sub { display: block; font-size: 22px; letter-spacing: 0.8px; padding-left: 4px; }

  .card--front .wordmark { left: 50%; top: 50%; transform: translate(-50%, -50%); }
  .card--front .wordmark__name { color: var(--white); }
  .card--back .wordmark { left: 34px; top: 40px; }
  .card--back .wordmark__name { color: var(--ink-purple); }
  .card--back .wordmark__main { font-size: 36px; }
  .card--back .wordmark__sub { font-size: 20px; }

  .holder {
    position: absolute;
    right: 34px;
    top: 44px;
    text-align: right;
  }
  .holder__name {
    font-family: "Questrial", sans-serif;
    font-size: 24px;
    color: var(--ink-purple);
    -webkit-text-stroke: 0.7px var(--ink-purple);
  }
  .holder__role {
    font-size: 16px;
    color: var(--rose);
    margin-top: 2px;
  }

  .contacts {
    position: absolute;
    left: 34px;
    bottom: 28px;
    list-style: none;
  }
  .contacts__item {
    display: flex;
    align-items: center;
    gap: 10px;
    font-size: 16px;
    color: var(--ink-purple);
    letter-spacing: 0.6px;
    line-height: 27px;
  }
  .contacts__icon { width: 16px; height: 16px; flex: none; fill: var(--teal); }
</style>
</head>
<body>
  <section class="card card--front" aria-label="Card front">
    <div class="wordmark">
      <span class="wordmark__dot"></span>
      <span class="wordmark__name"><span class="wordmark__main">Brightway</span><span class="wordmark__sub">Elder Assist</span></span>
    </div>
  </section>

  <section class="card card--back" aria-label="Card back">
    <div class="wordmark">
      <span class="wordmark__dot"></span>
      <span class="wordmark__name"><span class="wordmark__main">Brightway</span><span class="wordmark__sub">Elder Assist</span></span>
    </div>

    <div class="holder">
      <p class="holder__name">Dessa Quillan</p>
      <p class="holder__role">Owner</p>
    </div>

    <ul class="contacts">
      <li class="contacts__item">
        <svg class="contacts__icon" viewBox="0 0 24 24"><path d="M6.6 10.8a15.1 15.1 0 0 0 6.6 6.6l2.2-2.2c.3-.3.7-.4 1-.2 1.1.4 2.3.6 3.6.6.6 0 1 .4 1 1V20c0 .6-.4 1-1 1A17 17 0 0 1 3 4c0-.6.4-1 1-1h3.5c.6 0 1 .4 1 1 0 1.3.2 2.5.6 3.6.1.3 0 .7-.2 1z"/></svg>
        555.304.2291
      </li>
      <li class="contacts__item">
        <svg class="contacts__icon" viewBox="0 0 24 24"><path d="M2 5h20v14H2zm2 2v.5l8 5 8-5V7zm0 2.8V17h16V9.8l-8 5z"/></svg>
        Dessa@brightwayelderassist.example
      </li>
      <li class="contacts__item">
        <svg class="contacts__icon" viewBox="0 0 24 24"><path d="M12 2a10 10 0 1 0 0 20 10 10 0 0 0 0-20zm6.9 6h-3a15.7 15.7 0 0 0-1.3-3.9A8 8 0 0 1 18.9 8zM12 4c.8 1.2 1.5 2.5 1.9 4h-3.8c.4-1.5 1.1-2.8 1.9-4zM4.3 14a8 8 0 0 1 0-4h3.4a16.5 16.5 0 0 0 0 4zm.8 2h3a15.7 15.7 0 0 0 1.3 3.9A8 8 0 0 1 5.1 16zm3-8h-3a8 8 0 0 1 4.3-3.9C8.8 5.3 8.4 6.6 8.1 8zM12 20c-.8-1.2-1.5-2.5-1.9-4h3.8c-.4 1.5-1.1 2.8-1.9 4zm2.3-6H9.7a14.7 14.7 0 0 1 0-4h4.6a14.7 14.7 0 0 1 0 4zm.3 5.9c.6-1.2 1-2.5 1.3-3.9h3a8 8 0 0 1-4.3 3.9zm1.7-5.9a16.5 16.5 0 0 0 0-4h3.4a8 8 0 0 1 0 4z"/></svg>
        www.BrightwayElderAssist.example
      </li>
      <li class="contacts__item">
        <svg class="contacts__icon" viewBox="0 0 24 24"><path d="M12 2a7 7 0 0 0-7 7c0 5.2 7 13 7 13s7-7.8 7-13a7 7 0 0 0-7-7zm0 9.5a2.5 2.5 0 1 1 0-5 2.5 2.5 0 0 1 0 5z"/></svg>
        Cedarvale, Texas
      </li>
    </ul>
  </section>
</body>
</html>
```